Rebrand of an existing product label

We are looking for a new design / label for our body lotion. Attached is the current product label. We have this product available in Retinol, Collagen, Hyaluronic Acid, Vitamin C, and Coconut. The brand should reflect a clinical, trustworthy look. We also want to include on the label that the product contains Dead Sea Minerals. Attached is the dieline for the label for the jar and the top. This jar is the packaging that needs to be used for this project.
Updates

Target Market(s)

40+

Requirements
Must have
• Ingredient callouts on the front + benefits. Ex- Vitamin C Brightening Cream

```html
<!DOCTYPE html>
<html lang="en">
<head>
<meta charset="utf-8">
<title>Vitamin C Brightening Cream – Jar and Lid Labels</title>
<link rel="stylesheet" href="https://fonts.googleapis.com/css2?family=Jost:wght@400;500&display=swap">
<style>
  :root {
    --ink: #1f1f1f;
    --orange: #f59c20;
    --orange-deep: #e8901f;
    --label-light: #fafafa;
    --label-shade: #e6e6e8;
    --paper: #ffffff;
    --cream-text: #fff6ea;
  }
  * { margin: 0; padding: 0; box-sizing: border-box; }
  html, body { width: 918px; height: 1200px; overflow: hidden; background: var(--paper); }
  .canvas { position: relative; width: 918px; height: 1200px; font-family: "Jost", "Futura", sans-serif; color: var(--ink); }

  .jar-label {
    position: absolute; left: 216px; top: 316px; width: 497px; height: 331px;
    background: linear-gradient(90deg, var(--label-light) 0%, #f2f2f3 45%, var(--label-shade) 100%);
    border: 1px solid #e4e4e6;
  }
  .brand-vertical {
    position: absolute; left: 263px; top: 480px; width: 280px;
    transform: translate(-50%, -50%) rotate(-90deg); transform-origin: center;
    left: 285px;
    text-align: center; font-size: 31px; font-weight: 400; letter-spacing: 2px; color: var(--ink);
  }
  .product-name {
    position: absolute; left: 365px; top: 355px; font-size: 46px; font-weight: 400; letter-spacing: 0.5px; line-height: 1;
  }
  .benefit-pill {
    position: absolute; left: 350px; top: 414px; width: 273px; height: 32px; border-radius: 16px;
    background: var(--orange-deep); color: var(--cream-text);
    font-size: 21px; line-height: 32px; padding-left: 14px; letter-spacing: 0.3px;
  }
  .description {
    position: absolute; left: 363px; top: 471px; font-size: 21px; line-height: 27px; letter-spacing: 0.4px;
  }
  .mineral-callout {
    position: absolute; left: 363px; top: 535px; font-size: 18px; color: var(--orange-deep); letter-spacing: 0.2px;
  }
  .volume {
    position: absolute; left: 364px; top: 582px; font-size: 21px; letter-spacing: 0.3px;
  }

  .lid-label { position: absolute; left: 278px; top: 852px; width: 372px; height: 248px; }
  .lid-shape { fill: var(--orange); }
  .lid-brand { fill: var(--paper); font-family: "Jost", sans-serif; font-size: 15px; letter-spacing: 3px; }
  .lid-name { fill: var(--paper); font-family: "Jost", sans-serif; font-size: 38px; }
  .lid-benefit { fill: var(--paper); font-family: "Jost", sans-serif; font-size: 11.5px; }
  .lid-arc-text { fill: var(--paper); font-family: "Jost", sans-serif; font-size: 13px; letter-spacing: 3px; }
</style>
</head>
<body>
<main class="canvas">
  <section class="jar-label">
  </section>
  <div class="brand-vertical">VELORIA</div>
  <h1 class="product-name">VITAMIN C</h1>
  <div class="benefit-pill">BRIGHTENING CREAM</div>
  <p class="description">MOISTURIZING CREAM<br>FACE, NECK &amp; HANDS</p>
  <p class="mineral-callout">INFUSED WITH DEAD SEA MINERALS</p>
  <p class="volume">16.9 FL OZ (500 ML)</p>

  <svg class="lid-label" viewBox="0 0 372 248" xmlns="http://www.w3.org/2000/svg">
    <defs>
      <path id="lid-arc" d="M 19 104 A 172 172 0 0 0 353 104"/>
    </defs>
    <path class="lid-shape" d="M 60 0 C 25 0 0 30 0 70 L 0 80 C 0 180 85 246 186 246 C 287 246 372 180 372 80 L 372 70 C 372 30 347 0 312 0 C 285 0 272 15 260 30 C 240 52 215 66 186 66 C 157 66 132 52 112 30 C 100 15 87 0 60 0 Z"/>
    <text class="lid-brand" x="186" y="120" text-anchor="middle">VELORIA</text>
    <text class="lid-name" x="186" y="164" text-anchor="middle">VITAMIN C</text>
    <text class="lid-benefit" x="186" y="183" text-anchor="middle">BRIGHTENING CREAM</text>
    <text class="lid-arc-text">
      <textPath href="#lid-arc" startOffset="50%" text-anchor="middle">MOISTURIZING CREAM FACE, NECK &amp; HANDS</textPath>
    </text>
  </svg>
</main>
</body>
</html>
```